Consulting Company Business Card

I am looking for a minimalist, classy, professional design on my business card. I would like it to be double-sided. I want to use the font and color scheme of my logo which are attached. Please be creative in the designs that you send me. I want to play off the design of my logo with the inner C that is Green and Blue broken up with the white.
Target Market(s)
Small Businesses
Industry/Entity Type
Consulting
Contact Information for Business Card
Derek L. Whitmore, CPA CGMA, 555-014-2283, dwhitmore@brovantadvisory.example, www.brovantadvisory.example

```html
<!DOCTYPE html>
<html lang="en">
<head>
<meta charset="utf-8">
<title>Brovant Advisory – Business Card</title>
<link rel="stylesheet" href="https://fonts.googleapis.com/css2?family=Montserrat:wght@400;500;600;700&display=swap">
<style>
  :root {
    --teal: #237f82;
    --navy: #1f2448;
    --paper: #ffffff;
    --stage: #d9dadc;
    --ink-soft: #2b2f3a;
  }
  * { box-sizing: border-box; margin: 0; padding: 0; }
  html, body { width: 1200px; height: 801px; overflow: hidden; }
  body {
    background: var(--stage);
    font-family: "Montserrat", sans-serif;
    display: flex;
    align-items: center;
    justify-content: center;
    gap: 60px;
  }
  .card {
    width: 520px;
    height: 298px;
    border-radius: 18px;
    position: relative;
    overflow: hidden;
    box-shadow: 0 10px 28px rgba(0,0,0,0.18);
  }

  /* Front */
  .card-front {
    background: var(--teal);
    color: var(--paper);
    display: flex;
    flex-direction: column;
    align-items: center;
    justify-content: center;
  }
  .wordmark {
    display: flex;
    align-items: center;
    gap: 14px;
    font-weight: 700;
    letter-spacing: 0.02em;
    line-height: 1;
  }
  .wordmark-dot {
    width: 22px; height: 22px; border-radius: 50%;
    background: currentColor;
  }
  .wordmark-name { font-size: 40px; }
  .wordmark-sub {
    display: block;
    font-size: 15px;
    letter-spacing: 0.35em;
    margin-top: 8px;
  }
  .front-url {
    margin-top: 30px;
    font-size: 14px;
    font-weight: 500;
    letter-spacing: 0.06em;
  }

  /* Back */
  .card-back {
    background: var(--paper);
    display: flex;
    align-items: center;
  }
  .back-brand {
    width: 250px;
    display: flex;
    justify-content: center;
    color: var(--navy);
    padding-bottom: 20px;
  }
  .back-brand .wordmark { gap: 10px; }
  .back-brand .wordmark-dot { width: 16px; height: 16px; }
  .back-brand .wordmark-name { font-size: 28px; }
  .back-brand .wordmark-sub { font-size: 11px; margin-top: 6px; }

  .divider {
    width: 16px;
    height: 170px;
    position: relative;
    margin-bottom: 20px;
  }
  .divider::before {
    content: ""; position: absolute; left: 3px; top: 0; bottom: 0;
    width: 1px; background: var(--navy);
  }
  .divider::after {
    content: ""; position: absolute; left: 2px; top: 40px; height: 80px;
    width: 3px; background: var(--teal);
  }

  .contact-block { padding-left: 18px; padding-bottom: 20px; }
  .person-name {
    color: var(--teal);
    font-weight: 700;
    font-size: 20px;
    letter-spacing: 0.03em;
    text-transform: uppercase;
  }
  .person-title {
    color: var(--ink-soft);
    font-size: 11px;
    margin-top: 4px;
  }
  .name-rule {
    width: 80px; height: 2px; background: var(--teal);
    margin: 8px 0 12px;
  }
  .contact-list { list-style: none; }
  .contact-list li {
    display: flex; align-items: center; gap: 8px;
    font-size: 11px; color: var(--ink-soft);
    margin-bottom: 8px;
  }
  .contact-list svg { width: 12px; height: 12px; fill: var(--teal); flex: none; }

  .base-band {
    position: absolute; left: 0; right: 0; bottom: 0; height: 12px;
    display: flex;
  }
  .base-band .band-navy { flex: 0 0 62%; background: var(--navy); }
  .base-band .band-teal { flex: 1; background: var(--teal); margin-left: 4px; }
</style>
</head>
<body>

  <section class="card card-front" aria-label="Card front">
    <div class="wordmark">
      <span class="wordmark-dot"></span>
      <span class="wordmark-name">BROVANT<span class="wordmark-sub">ADVISORY</span></span>
    </div>
    <p class="front-url">www.brovantadvisory.example</p>
  </section>

  <section class="card card-back" aria-label="Card back">
    <div class="back-brand">
      <div class="wordmark">
        <span class="wordmark-dot"></span>
        <span class="wordmark-name">BROVANT<span class="wordmark-sub">ADVISORY</span></span>
      </div>
    </div>
    <div class="divider"></div>
    <div class="contact-block">
      <h1 class="person-name">Derek L. Whitmore</h1>
      <p class="person-title">CPA CGMA</p>
      <div class="name-rule"></div>
      <ul class="contact-list">
        <li>
          <svg viewBox="0 0 24 24" aria-hidden="true"><path d="M6.6 10.8a15 15 0 0 0 6.6 6.6l2.2-2.2a1 1 0 0 1 1-.25 11.4 11.4 0 0 0 3.6.6 1 1 0 0 1 1 1V20a1 1 0 0 1-1 1A17 17 0 0 1 3 4a1 1 0 0 1 1-1h3.5a1 1 0 0 1 1 1c0 1.25.2 2.45.6 3.6a1 1 0 0 1-.25 1z"/></svg>
          555-014-2283
        </li>
        <li>
          <svg viewBox="0 0 24 24" aria-hidden="true"><path d="M2 5h20v14H2z M4 7v.5l8 5 8-5V7l-8 5z" fill-rule="evenodd"/></svg>
          dwhitmore@brovantadvisory.example
        </li>
        <li>
          <svg viewBox="0 0 24 24" aria-hidden="true"><circle cx="12" cy="12" r="10"/></svg>
          www.brovantadvisory.example
        </li>
      </ul>
    </div>
    <div class="base-band"><span class="band-navy"></span><span class="band-teal"></span></div>
  </section>

</body>
</html>
```